Super-fantastic-interesting infographic of terribly boring content

-Looking to provide a visually engaging snapshot of the average Canadian investor.
-Help people compare their personal financial situation against the infographic (Average).
-We want viewers to feel engaged and interested in the info presented, not confused and irritated.

Data points to present:

The average Canadian snapshot:
* Average Canadian household Income in 2016: $76,900
* Median Net Worth of Canadian families in 2016: $295,100
* Average annual household expenditures on goods a& services: $62,183
* Median value in principal residence: $349,000
* Highest net annual savings amount (Age 35-44): $10,120
* Number of Canadian families holding a mortgage: 38.4%
* Median Mortgage value of Principal residence: $190,000
* Debt to disposable income ratio average: 172.1
* Total value of all assets held by Canadians in 2016: 12 Trillion dollars
* The principal residence was the single largest asset held (of the 12 Trillion): 32%
* Private pensions was the 2nd largest grouping of assets at 29.2%
* The average borrowing rate for Canadian mortgages: 2.94%
* 74% were fixed rate, 21% were variable and 5% blended.
* 48% of Canadians do not save or invest at all
* 54% of Canadians do not budget regularly
* 1 in 3 Canadians have lost at least 20% in one year
* 51% of Canadians took NO ACTION after losing at least 20% in one year.
* 22% of those people either, hired or fired an advisor

Financial advice landscape:
* # of households in Canada: 13,300,000
* Households with an advisor 5,300,000
* % of households dissatisfied with existing advisor 1,100,000

Target Market(s)

Investors, ages 22-55

Industry/Entity Type

Financial

Font styles to use
Sans Serif

Colors

Designer to choose colors to be used in the design.

Requirements
Must have
• Header: Financial landscape of the average Canadian
Nice to have
• There is a lot of numbers and percentages, find a way to deliver the info using a mix of images, numbers, pictures etc.

```html
<!DOCTYPE html>
<html lang="en">
<head>
<meta charset="utf-8">
<title>Financial Landscape of the Average Canadian</title>
<link href="https://fonts.googleapis.com/css2?family=Lato:wght@400;700;900&display=swap" rel="stylesheet">
<style>
  :root{
    --page:#efefef; --frame:#e5262a; --paper:#ffffff; --band:#fafae6;
    --ink:#111111; --note:#7a7a7a; --rule:#c9d3d9;
    --teal:#29b6c8; --salmon:#f4826f; --slate:#5d6470; --mist:#c9d3d9;
    --green:#8fcf7f; --violet:#9b7cc4; --lime:#dfe37e; --pink:#e8357a;
    --coin:#f9c04b;
  }
  html,body{margin:0;width:1200px;height:1200px;overflow:hidden;background:var(--page);}
  .poster{position:absolute;left:282px;top:26px;width:638px;height:1147px;display:block;}
  svg text{font-family:'Lato',sans-serif;}
  .brand{font-size:42px;font-weight:400;fill:#3a3a3a;}
  .title{font-size:33px;font-weight:900;fill:var(--ink);text-anchor:middle;}
  .title-accent{fill:var(--frame);}
  .section{font-size:24px;font-weight:900;fill:var(--ink);text-anchor:middle;}
  .dash{stroke:var(--frame);stroke-width:3;stroke-dasharray:15 10;fill:none;}
  .track{stroke:var(--rule);stroke-width:2;fill:none;}
  .end{fill:#fff;stroke:var(--rule);stroke-width:2;}
  .note{font-size:8px;fill:var(--note);text-anchor:middle;}
  .pct{font-size:6px;fill:var(--pink);text-anchor:middle;font-weight:700;}
  .dollar{font-size:17px;font-weight:900;fill:#2b2b2b;text-anchor:middle;}
  .arc{fill:none;stroke:var(--pink);stroke-width:2;}
  .card{fill:#fff;stroke:#e2e2e2;}
</style>
</head>
<body>
<svg class="poster" viewBox="352 33 797 1433" xmlns="http://www.w3.org/2000/svg">
  <defs>
    <g id="coin">
      <circle r="14" fill="var(--coin)"/>
      <circle r="11" fill="none" stroke="#2b2b2b" stroke-width="1" stroke-dasharray="2 3"/>
      <text class="dollar" y="6">$</text>
    </g>
    <g id="bars">
      <circle r="10" fill="#fff"/>
      <rect x="-5" y="-1" width="2.5" height="6" fill="var(--teal)"/>
      <rect x="-1" y="-5" width="2.5" height="10" fill="var(--salmon)"/>
      <rect x="3" y="-3" width="2.5" height="8" fill="var(--slate)"/>
    </g>
  </defs>

  <!-- frame -->
  <rect x="352" y="33" width="797" height="1433" fill="var(--frame)"/>
  <rect x="375" y="56" width="751" height="1387" fill="var(--paper)"/>

  <!-- brand -->
  <circle cx="632" cy="134" r="34" fill="#2a6fc0"/>
  <text class="brand" x="680" y="146">TrueLedger</text>

  <!-- title band -->
  <rect x="375" y="195" width="751" height="5" fill="var(--frame)"/>
  <rect x="375" y="200" width="751" height="106" fill="var(--band)"/>
  <rect x="375" y="306" width="751" height="5" fill="var(--frame)"/>
  <text class="title" x="754" y="245">FINANCIAL LANDSCAPE OF THE AVERAGE</text>
  <text class="title title-accent" x="754" y="287">CANADIAN</text>

  <!-- snapshot heading -->
  <rect x="468" y="338" width="28" height="28" fill="var(--frame)" role="img" aria-label="Maple leaf"/>
  <rect x="998" y="338" width="28" height="28" fill="var(--frame)" role="img" aria-label="Maple leaf"/>
  <text class="section" x="750" y="360">THE AVERAGE <tspan fill="var(--frame)">CANADIAN</tspan> SNAPSHOT</text>
  <line class="dash" x1="411" y1="394" x2="1085" y2="394"/>

  <!-- timeline path -->
  <path class="track" d="M415 512 H1085 V725 H415 V938 H842"/>
  <circle class="end" cx="415" cy="512" r="7"/>
  <circle class="end" cx="1085" cy="512" r="7"/>
  <circle class="end" cx="1085" cy="725" r="7"/>
  <circle class="end" cx="415" cy="725" r="7"/>
  <circle class="end" cx="415" cy="938" r="7"/>
  <circle class="end" cx="842" cy="938" r="7"/>

  <!-- row 1 -->
  <g class="row-one">
    <line class="track" x1="487" y1="475" x2="487" y2="512"/>
    <circle cx="487" cy="454" r="19" fill="#fff" stroke="var(--teal)" stroke-width="5"/><use href="#coin" x="487" y="454"/>
    <circle cx="487" cy="512" r="6" fill="var(--teal)"/>
    <text class="note" x="487" y="536">Average Canadian</text><text class="note" x="487" y="545">household Income in 2016:</text><text class="note" x="487" y="554">$76,900</text>

    <line class="track" x1="574" y1="512" x2="574" y2="549"/>
    <circle cx="574" cy="570" r="19" fill="#fff" stroke="var(--salmon)" stroke-width="5"/><use href="#coin" x="574" y="570"/>
    <circle cx="574" cy="512" r="6" fill="var(--salmon)"/>
    <text class="note" x="574" y="476">Median Net Worth of</text><text class="note" x="574" y="485">Canadian families in 2016:</text><text class="note" x="574" y="494">$295,100</text>

    <line class="track" x1="660" y1="475" x2="660" y2="512"/>
    <circle cx="660" cy="454" r="19" fill="#fff" stroke="var(--slate)" stroke-width="5"/><use href="#coin" x="660" y="454"/>
    <circle cx="660" cy="512" r="6" fill="var(--slate)"/>
    <text class="note" x="660" y="536">Average annual household</text><text class="note" x="660" y="545">expenditures on goods &amp;</text><text class="note" x="660" y="554">services: $62,183</text>

    <line class="track" x1="746" y1="512" x2="746" y2="549"/>
    <circle cx="746" cy="570" r="19" fill="#fff" stroke="var(--mist)" stroke-width="5"/><use href="#coin" x="746" y="570"/>
    <circle cx="746" cy="512" r="6" fill="var(--mist)"/>
    <text class="note" x="746" y="476">Median value in principal</text><text class="note" x="746" y="485">residence: $349,000</text>

    <line class="track" x1="833" y1="475" x2="833" y2="512"/>
    <circle cx="833" cy="454" r="19" fill="#fff" stroke="var(--green)" stroke-width="5"/><use href="#coin" x="833" y="454"/>
    <circle cx="833" cy="512" r="6" fill="var(--green)"/>
    <text class="note" x="833" y="536">Highest net annual savings</text><text class="note" x="833" y="545">amount (Age 35-44):</text><text class="note" x="833" y="554">$10,120</text>

    <line class="track" x1="920" y1="512" x2="920" y2="549"/>
    <circle cx="920" cy="570" r="19" fill="#fff" stroke="var(--violet)" stroke-width="5"/>
    <circle class="arc" cx="920" cy="570" r="14" stroke-dasharray="33.8 88" transform="rotate(-90 920 570)"/>
    <text class="pct" x="920" y="572">38.4%</text>
    <circle cx="920" cy="512" r="6" fill="var(--violet)"/>
    <text class="note" x="920" y="476">Number of Canadian</text><text class="note" x="920" y="485">families holding a</text><text class="note" x="920" y="494">mortgage: 38.4%</text>

    <line class="track" x1="1006" y1="475" x2="1006" y2="512"/>
    <circle cx="1006" cy="454" r="19" fill="#fff" stroke="var(--lime)" stroke-width="5"/><use href="#coin" x="1006" y="454"/>
    <circle cx="1006" cy="512" r="6" fill="var(--lime)"/>
    <text class="note" x="1006" y="536">Median Mortgage value of</text><text class="note" x="1006" y="545">Principal residence:</text><text class="note" x="1006" y="554">$190,000</text>
  </g>

  <!-- row 2 -->
  <g class="row-two">
    <line class="track" x1="494" y1="725" x2="494" y2="761"/>
    <circle cx="494" cy="782" r="19" fill="#fff" stroke="var(--lime)" stroke-width="5"/>
    <circle class="arc" cx="494" cy="782" r="14" stroke-dasharray="42.2 88" transform="rotate(-90 494 782)"/>
    <text class="pct" x="494" y="784">48%</text>
    <circle cx="494" cy="725" r="6" fill="var(--lime)"/>
    <text class="note" x="494" y="691">48% of Canadians do not</text><text class="note" x="494" y="700">save or invest at all</text>

    <line class="track" x1="581" y1="688" x2="581" y2="725"/>
    <circle cx="581" cy="667" r="19" fill="#fff" stroke="var(--violet)" stroke-width="5"/>
    <circle class="arc" cx="581" cy="667" r="14" stroke-dasharray="65.1 88" transform="rotate(-90 581 667)"/>
    <text class="pct" x="581" y="669">74%</text>
    <circle cx="581" cy="725" r="6" fill="var(--violet)"/>
    <text class="note" x="581" y="750">74% were fixed rate, 21%</text><text class="note" x="581" y="759">were variable and 5%</text><text class="note" x="581" y="768">blended.</text>

    <line class="track" x1="667" y1="725" x2="667" y2="761"/>
    <circle cx="667" cy="782" r="19" fill="#fff" stroke="var(--green)" stroke-width="5"/>
    <circle class="arc" cx="667" cy="782" r="14" stroke-dasharray="3 88" transform="rotate(-90 667 782)"/>
    <text class="pct" x="667" y="784">2.94%</text>
    <circle cx="667" cy="725" r="6" fill="var(--green)"/>
    <text class="note" x="667" y="691">The average borrowing rate</text><text class="note" x="667" y="700">for Canadian mortgages:</text><text class="note" x="667" y="709">2.94%</text>

    <line class="track" x1="754" y1="688" x2="754" y2="725"/>
    <circle cx="754" cy="667" r="19" fill="#fff" stroke="var(--mist)" stroke-width="5"/>
    <circle class="arc" cx="754" cy="667" r="14" stroke-dasharray="25.7 88" transform="rotate(-90 754 667)"/>
    <text class="pct" x="754" y="669">29.2%</text>
    <circle cx="754" cy="725" r="6" fill="var(--mist)"/>
    <text class="note" x="754" y="750">Private pensions was the</text><text class="note" x="754" y="759">2nd largest grouping of</text><text class="note" x="754" y="768">assets at 29.2%</text>

    <line class="track" x1="840" y1="725" x2="840" y2="761"/>
    <circle cx="840" cy="782" r="19" fill="#fff" stroke="var(--slate)" stroke-width="5"/>
    <circle class="arc" cx="840" cy="782" r="14" stroke-dasharray="28.2 88" transform="rotate(-90 840 782)"/>
    <text class="pct" x="840" y="784">32%</text>
    <circle cx="840" cy="725" r="6" fill="var(--slate)"/>
    <text class="note" x="840" y="691">The principal residence was</text><text class="note" x="840" y="700">the single largest asset held</text><text class="note" x="840" y="709">(of the 12 Trillion): 32%</text>

    <line class="track" x1="927" y1="688" x2="927" y2="725"/>
    <circle cx="927" cy="667" r="19" fill="#fff" stroke="var(--salmon)" stroke-width="5"/><use href="#coin" x="927" y="667"/>
    <circle cx="927" cy="725" r="6" fill="var(--salmon)"/>
    <text class="note" x="927" y="750">Total value of all assets</text><text class="note" x="927" y="759">held by Canadians in 2016:</text><text class="note" x="927" y="768">12 Trillion dollars</text>

    <line class="track" x1="1013" y1="725" x2="1013" y2="761"/>
    <circle cx="1013" cy="782" r="19" fill="#fff" stroke="var(--teal)" stroke-width="5"/><use href="#coin" x="1013" y="782"/>
    <circle cx="1013" cy="725" r="6" fill="var(--teal)"/>
    <text class="note" x="1013" y="691">Debt to disposable income</text><text class="note" x="1013" y="700">ratio average: 172.1</text>
  </g>

  <!-- row 3 -->
  <g class="row-three">
    <line class="track" x1="487" y1="901" x2="487" y2="938"/>
    <circle cx="487" cy="880" r="19" fill="#fff" stroke="var(--teal)" stroke-width="5"/>
    <circle class="arc" cx="487" cy="880" r="14" stroke-dasharray="47.5 88" transform="rotate(-90 487 880)"/>
    <text class="pct" x="487" y="882">54%</text>
    <circle cx="487" cy="938" r="6" fill="var(--teal)"/>
    <text class="note" x="487" y="961">54% of Canadians do not</text><text class="note" x="487" y="970">budget regularly</text>

    <line class="track" x1="574" y1="938" x2="574" y2="975"/>
    <circle cx="574" cy="996" r="19" fill="#fff" stroke="var(--salmon)" stroke-width="5"/>
    <circle class="arc" cx="574" cy="996" r="14" stroke-dasharray="17.6 88" transform="rotate(-90 574 996)"/>
    <text class="pct" x="574" y="998">20%</text>
    <circle cx="574" cy="938" r="6" fill="var(--salmon)"/>
    <text class="note" x="574" y="911">1 in 3 Canadians have lost</text><text class="note" x="574" y="920">at least 20% in one year</text>

    <line class="track" x1="660" y1="901" x2="660" y2="938"/>
    <circle cx="660" cy="880" r="19" fill="#fff" stroke="var(--slate)" stroke-width="5"/>
    <circle class="arc" cx="660" cy="880" r="14" stroke-dasharray="44.9 88" transform="rotate(-90 660 880)"/>
    <text class="pct" x="660" y="882">51%</text>
    <circle cx="660" cy="938" r="6" fill="var(--slate)"/>
    <text class="note" x="660" y="961">51% of Canadians took NO</text><text class="note" x="660" y="970">ACTION after losing at least</text><text class="note" x="660" y="979">20% in one year.</text>

    <line class="track" x1="746" y1="938" x2="746" y2="975"/>
    <circle cx="746" cy="996" r="19" fill="#fff" stroke="var(--mist)" stroke-width="5"/>
    <circle class="arc" cx="746" cy="996" r="14" stroke-dasharray="19.4 88" transform="rotate(-90 746 996)"/>
    <text class="pct" x="746" y="998">22%</text>
    <circle cx="746" cy="938" r="6" fill="var(--mist)"/>
    <text class="note" x="746" y="911">22% of those people either,</text><text class="note" x="746" y="920">hired or fired an advisor</text>
  </g>

  <rect x="915" y="848" width="132" height="180" rx="6" fill="url(#stackFill)" role="img" aria-label="Stacked layers illustration"/>
  <linearGradient id="stackFill" x1="0" y1="0" x2="0" y2="1">
    <stop offset="0" stop-color="#29afd0"/><stop offset="0.4" stop-color="#e5579f"/>
    <stop offset="0.65" stop-color="#f28a33"/><stop offset="1" stop-color="#a8b3b5"/>
  </linearGradient>

  <!-- advice section -->
  <line class="dash" x1="411" y1="1060" x2="1085" y2="1060"/>
  <rect x="500" y="1086" width="28" height="28" fill="var(--frame)" role="img" aria-label="Maple leaf"/>
  <rect x="967" y="1086" width="28" height="28" fill="var(--frame)" role="img" aria-label="Maple leaf"/>
  <text class="section" x="750" y="1108">FINANCIAL ADVICE LANDSCAPE</text>
  <line class="dash" x1="411" y1="1142" x2="1085" y2="1142"/>

  <rect x="400" y="1165" width="250" height="255" rx="14" fill="url(#mapFill)" role="img" aria-label="Map of Canada with a flag planted on it"/>
  <linearGradient id="mapFill" x1="0" y1="0" x2="1" y2="1">
    <stop offset="0" stop-color="#e9a3a3"/><stop offset="0.3" stop-color="#7ea53a"/><stop offset="1" stop-color="#4e7a22"/>
  </linearGradient>

  <line class="track" x1="893" y1="1195" x2="893" y2="1393"/>
  <circle class="end" cx="893" cy="1195" r="4"/><circle class="end" cx="893" cy="1393" r="4"/>
  <line class="track" x1="870" y1="1237" x2="893" y2="1237"/>
  <line class="track" x1="870" y1="1336" x2="893" y2="1336"/>
  <line class="track" x1="893" y1="1287" x2="916" y2="1287"/>
  <circle cx="893" cy="1237" r="3" fill="var(--rule)"/><circle cx="893" cy="1336" r="3" fill="var(--rule)"/><circle cx="893" cy="1287" r="3" fill="var(--rule)"/>

  <circle cx="860" cy="1237" r="12" fill="#fff" stroke="var(--teal)" stroke-width="3"/><use href="#bars" x="860" y="1237"/>
  <circle cx="860" cy="1336" r="12" fill="#fff" stroke="var(--slate)" stroke-width="3"/><use href="#bars" x="860" y="1336"/>
  <circle cx="927" cy="1287" r="12" fill="#fff" stroke="var(--salmon)" stroke-width="3"/><use href="#bars" x="927" y="1287"/>

  <rect class="card" x="696" y="1205" width="132" height="73"/>
  <text class="note" x="762" y="1242">#of households in Canada:</text><text class="note" x="762" y="1251">13,300,000</text>
  <rect class="card" x="696" y="1303" width="132" height="74"/>
  <text class="note" x="762" y="1330">% of households</text><text class="note" x="762" y="1339">dissatisfied with existing</text><text class="note" x="762" y="1348">advisor 1,100,000</text>
  <rect class="card" x="956" y="1255" width="131" height="73"/>
  <text class="note" x="1029" y="1289">Households with an advisor</text><text class="note" x="1029" y="1298">5,300,000</text>
</svg>
</body>
</html>
```